依頼概要
■依頼目的 / 概要
電子書籍Lumora本を出版いたしますので、
表紙デザイン作成をお願いいたします。

■納品物
下記での納品をお願い致します。

JPEG形式 及び PSD形式
横1600ピクセル x 縦2560ピクセル

■本の内容

<本のタイトル>
ソラノワ-SKY RING-
老職人に学んだ
はじめての家庭づくりのガイドブック

<著者名>
浅井徹郎

■デザイン要望
・本のタイトル / 著者名の反映をお願いします

デザインイメージ

・基本的に青系の色合い

・シンプルな背景にタイトル等のコピーを記載

・ターゲットは子どもを持つご両親。

・お子様の子育てに関する細かいノウハウというよりも、
最も要となる考え方をお伝えしています。

・信頼感のあるデザインを希望します。

<表現したいイメージなど>
・信頼感

<表現したくないイメージ>
・安っぽい
・嘘くさい
・大衆的

<利用画像について>
画像素材を使用される場合には、
商用利用可の素材をお願いします。

■その他
デザインを考えるのに必要な情報が他にございましたら、
お答えしますので、遠慮なくご連絡ください。

*添付ファイルは、過去電子書籍の表紙デザインです。
*ジャンルが異なりますので、デザインテイストは今回とは、異なります。
*あくまでも、表紙に出てくる要素(タイトルや著者名など)の参考としてご利用ください。

意図をしっかりとご理解いただき、
目につく素晴らしいデザインに仕上げていただきました。
ありがとうございます。

この度は応募いただきありがとうございました。
近いうちにまた同じく、表紙のデザインをお願いする予定です。
またご参加くださいませ。

```html
<!DOCTYPE html>
<html lang="ja">
<head>
<meta charset="utf-8">
<title>ソラノワ -SKY RING- 表紙</title>
<link rel="stylesheet" href="https://fonts.googleapis.com/css2?family=Playfair+Display:wght@700;900&family=Noto+Serif+JP:wght@600;700&family=Noto+Sans+JP:wght@700&display=swap">
<style>
  :root {
    --royal-blue: #22409c;
    --stripe-blue: #1d378a;
    --gold: #c8ac69;
    --white: #ffffff;
    --navy-ink: #1e2870;
    --paper: #ffffff;
  }
  html, body {
    margin: 0;
    padding: 0;
    width: 750px;
    height: 1200px;
    overflow: hidden;
    background: var(--paper);
  }
  .cover {
    position: relative;
    width: 750px;
    height: 1200px;
    overflow: hidden;
    background: var(--paper);
  }
  .cover-band {
    position: absolute;
    left: 0; top: 0;
    width: 750px; height: 575px;
    background:
      repeating-linear-gradient(135deg,
        var(--royal-blue) 0 6px,
        var(--stripe-blue) 6px 9px);
  }
  .title-en {
    position: absolute;
    left: 30px;
    top: 0;
    margin: 0;
    font-family: "Playfair Display", "Times New Roman", serif;
    font-weight: 900;
    color: var(--gold);
    line-height: 1;
    letter-spacing: -2px;
    transform: scaleY(1.2);
    transform-origin: top left;
  }
  .title-en .line-one { position: absolute; top: 18px; font-size: 200px; white-space: nowrap; }
  .title-en .line-two { position: absolute; top: 225px; font-size: 200px; white-space: nowrap; }
  .title-kana {
    position: absolute;
    left: 470px;
    top: 92px;
    font-family: "Noto Sans JP", sans-serif;
    font-weight: 700;
    font-size: 38px;
    color: var(--white);
    letter-spacing: 1px;
  }
  .author-roman {
    position: absolute;
    left: 36px;
    top: 498px;
    font-family: "Noto Sans JP", sans-serif;
    font-weight: 700;
    font-size: 22px;
    color: var(--white);
  }
  .author-name {
    position: absolute;
    left: 34px;
    top: 522px;
    font-family: "Noto Serif JP", serif;
    font-weight: 700;
    font-size: 40px;
    color: var(--white);
    letter-spacing: 2px;
  }
  .line-art {
    position: absolute;
    z-index: 1;
    left: 487px;
    top: 760px;
    width: 263px;
    height: 420px;
    background: radial-gradient(ellipse at 55% 50%, #f3eef4 0%, #ffffff 70%);
  }
  .subtitle {
    position: absolute;
    z-index: 2;
    left: 292px;
    top: 588px;
    margin: 0;
    font-family: "Noto Serif JP", serif;
    font-weight: 700;
    font-size: 62px;
    line-height: 100px;
    color: var(--navy-ink);
    white-space: nowrap;
  }
</style>
</head>
<body>
  <main class="cover">
    <div class="cover-band"></div>
    <h1 class="title-en" aria-label="SKY RING">
      <span class="line-one">SKY</span>
      <span class="line-two">RING</span>
    </h1>
    <div class="title-kana">ソラノワ</div>
    <div class="author-roman">Asai Tetsurou</div>
    <div class="author-name">浅井徹郎</div>
    <div class="line-art" role="img" aria-label="家族の寄り添う姿を描いた細い線画のイラスト"></div>
    <p class="subtitle">老職人に<br>学んだ<br>はじめての<br>家庭づくりの<br>ガイドブック</p>
  </main>
</body>
</html>
```